Corporate Website Homepage design

Looking for a design of a Corporate Website, Velkor Pty Ltd. Existing website is quite old, and outdated: www.velkor-example.com.au

Our company has two sides, with consumer facing brands and services for clients to develop their own brands, referred to as Private Label.

Looking for a premium design that incorporates both our services as private label and sourcing specialists, from a corporate side. And also information about our own brands, and a link to a webshop where they can be purchased.

Example General Structure:
Top Menu bar and Logo
Rotating Banner

About Our Services (well presented section of below services, with small descriptions below each one, and space to click through to learn more on each):
- Global Sourcing, Distribution & Supply Solutions
- Specialist Private Label Manufacturing Facilities
- Strict Quality Assurance Processes & Certifications

Brands:
• Wimbletots – Fun & Amazing Value range of baby Clothing, Manchester and Accessories
• Lunorella – Luxurious Organic Baby Clothing, Wraps and Accessories
• Tinyharbor – Everything Baby at Amazing Prices
• Faxlo Infant – Infant Feeding range with all your favourite Faxlo Characters
• WovenHarvests – Luxury range of Towels and Manchester
• ZigzagKite – Exciting range of Kids Clothing, with a twist

Product Categories:
Infant Feeding and Accessories
Infant Clothing
Infant Gear
Maternity Wear
Mens Underwear
Homewares and Manchester

Target Market(s)

Corporate Customers - Retailer buyers and Consumers looking for brand information

Industry/Entity Type

Baby

Requirements
Must have
• Good structure split by
Services, Brands and Product to allow people looking for particular things to find them quickly due to different types of visitors (corporate vs consumer)

Clean and Professional Design

with information, should have links to blog, webshop

```html
<!DOCTYPE html>
<html lang="en">
<head>
<meta charset="utf-8">
<title>Velkor International</title>
<link href="https://fonts.googleapis.com/css2?family=PT+Sans:wght@400;700&family=PT+Sans+Narrow:wght@400;700&family=Oswald:wght@500&family=Courgette&display=swap" rel="stylesheet">
<style>
:root{
  --red:#e8001f;
  --blue:#0b6fc1;
  --sky:#10a8f0;
  --orange:#f05a0a;
  --orange-soft:#f37b2a;
  --green:#79b30f;
  --green-bright:#8cc318;
  --teal:#2ccfd4;
  --ink:#333;
  --muted:#555;
  --line:#ddd;
  --card:#f6f6f6;
  --footer:#f1f1f1;
}
*{box-sizing:border-box;margin:0;padding:0}
html,body{width:720px;height:1200px;overflow:hidden;background:#fff}
body{font-family:"PT Sans",sans-serif;color:var(--ink);position:relative}
.abs{position:absolute}
.topstrip{top:0;left:0;width:720px;height:3px;background:linear-gradient(90deg,#2ab0e4 0 17%,#f39b16 17% 34%,#e2208a 34% 51%,#7cbd2a 51% 68%,#2ab0e4 68% 84%,#f39b16 84%)}
.logo{left:62px;top:16px;width:88px;height:56px;display:flex;align-items:center;gap:6px}
.logo-dot{width:14px;height:14px;border-radius:50%;background:var(--blue)}
.logo-name{font-size:22px;font-weight:700;color:var(--blue)}
.follow{right:60px;top:16px;display:flex;align-items:center;gap:6px;font-size:13px}
.follow i{display:block;width:18px;height:18px;border-radius:3px}
.call{left:322px;top:52px;font-size:15px}
.call b{font-weight:400;color:var(--red);font-family:Georgia,serif}
.search{left:495px;top:50px;width:165px;height:21px;border:1px solid #ccc;border-radius:2px;font-size:8px;font-style:italic;color:#999;padding:5px 7px}
.search svg{position:absolute;right:5px;top:4px}
.nav{left:0;top:83px;width:720px;height:23px;background:var(--red);border-bottom:1px dashed #fff;box-shadow:0 2px 0 var(--red)}
.nav ul{list-style:none;display:flex;position:absolute;left:68px;top:0}
.nav li{color:#fff;font-size:10.5px;line-height:23px;padding:0 0}
.banner{left:59px;top:122px;width:601px;height:240px;border:1px solid #ddd;background:#fff;padding:6px;box-shadow:0 1px 3px rgba(0,0,0,.15)}
.banner-inner{position:relative;width:100%;height:100%;background:linear-gradient(90deg,#37c6cc,#30d3d6 60%,#28c9d0)}
.banner-photo{position:absolute;left:0;top:0;width:395px;height:100%;background:radial-gradient(ellipse at 30% 40%,#f2c7a5 0 18%,transparent 19%),radial-gradient(ellipse at 75% 45%,#f06a6a 0 14%,#f2b52a 15% 26%,transparent 27%),linear-gradient(90deg,#4fc9c9,#3fcad0)}
.banner-title{position:absolute;right:16px;top:30px;font-family:"Courgette",cursive;font-size:34px;color:#1560b0;text-align:right}
.banner-sub{position:absolute;right:17px;top:76px;font-size:20px;font-weight:700;color:#f6e21a}
.banner-text{position:absolute;right:17px;top:110px;width:200px;text-align:right;font-size:8.5px;font-weight:700;color:#fff;font-family:Arial,sans-serif;line-height:1.35}
.banner-btn{position:absolute;right:17px;top:147px;background:var(--orange);color:#fff;font-size:10.5px;font-weight:700;padding:4px 13px;border-radius:11px}
.dots{position:absolute;right:12px;bottom:9px;display:flex;gap:3px}
.dots i{width:9px;height:9px;border-radius:50%;background:#fff}
.dots i:first-child{background:var(--red)}
.heading{font-size:15px;color:#222;border-bottom:2px solid #e3e3e3;padding-bottom:5px}
.services{left:59px;top:378px;width:601px}
.service-row{left:59px;top:410px;width:601px;display:flex}
.service{flex:1;text-align:center;padding:0 3px;border-right:1px dashed #bbb;height:130px}
.service:last-child{border-right:0}
.service h3{font-family:"PT Sans Narrow",sans-serif;font-weight:400;font-size:11px;line-height:13.5px;text-transform:uppercase}
.service svg{display:block;margin:6px auto 7px}
.service p{font-family:Arial,sans-serif;font-size:6.8px;line-height:11px;color:var(--muted)}
.readmore{display:inline-block;margin-top:8px;color:#fff;font-size:7px;font-weight:700;padding:5px 16px 5px 16px;clip-path:polygon(0 0,88% 0,100% 50%,88% 100%,0 100%)}
.c-orange h3{color:var(--orange)}.c-orange .readmore{background:var(--orange)}
.c-blue h3{color:var(--sky)}.c-blue .readmore{background:var(--sky)}
.c-green h3{color:var(--green)}.c-green .readmore{background:var(--green)}
.featured{left:59px;top:560px;width:601px}
.arrows{right:60px;top:561px;color:var(--sky);font-size:16px;font-weight:700;letter-spacing:-1px}
.products{left:60px;top:591px;display:flex;gap:12.6px}
.product{width:90px;text-align:center;border-right:1px dashed #ccc;padding-right:0}
.product:last-child{border-right:0}
.product-img{width:90px;height:66px;border:1px solid #ddd}
.product-name{height:30px;display:flex;align-items:center;justify-content:center;font-size:8.5px;line-height:10.5px}
.viewmore{background:var(--sky);color:#fff;font-size:8.5px;line-height:18px;clip-path:polygon(0 0,92% 0,100% 50%,92% 100%,0 100%)}
.brands{left:59px;top:722px;width:373px}
.quick{left:450px;top:722px;width:210px}
.brand-grid{left:60px;top:756px;display:grid;grid-template-columns:180px 180px;gap:9px 12px}
.brand{height:60px;background:var(--card);border:1px solid #e2e2e2;border-radius:3px;box-shadow:0 1px 2px rgba(0,0,0,.12);display:flex;align-items:center;padding:0 6px;gap:8px}
.brand-name{width:68px;font-size:10px;font-weight:700;text-align:center;flex-shrink:0}
.brand p{font-family:Arial,sans-serif;font-size:6.8px;line-height:10px;color:#333}
.b1 .brand-name{color:#8a5a9c}.b2 .brand-name{color:var(--blue)}.b3 .brand-name{color:#d6284a}.b4 .brand-name{color:var(--blue)}.b5 .brand-name{color:#111}.b6 .brand-name{color:#1e74c0}
.tile{left:450px;width:210px;border-radius:2px;color:#fff;font-family:"Oswald",sans-serif}
.tile-blog{top:756px;height:95px;background:var(--orange-soft);border:1px solid #e05a10}
.tile-shop{top:858px;height:96px;background:var(--green-bright);border:1px solid #6a9f0c}
.tile svg{position:absolute}
.tile .big{position:absolute;font-size:31px;line-height:30px}
.tile .small{position:absolute;font-size:13px}
.footer{left:60px;top:985px;width:600px;height:200px;background:var(--footer);border-radius:5px}
.fcol{position:absolute;top:17px;font-size:6.8px;line-height:11px;color:#555;font-family:Arial,sans-serif}
.fcol h4{font-family:"PT Sans",sans-serif;font-weight:400;font-size:11px;color:#222;margin-bottom:6px}
.fcol ul{list-style:none}
.fcol li{margin-bottom:4.6px;padding-left:9px;position:relative}
.fcol li:before{content:"";position:absolute;left:0;top:3px;border-left:3px solid #555;border-top:2.5px solid transparent;border-bottom:2.5px solid transparent}
.fsep{position:absolute;top:20px;height:92px;border-left:1px dashed #ccc}
.payname{font-size:15px;font-weight:700;color:#1b4f9c;text-align:center;margin:2px 0 6px}
.cards{display:flex;gap:3px;justify-content:center;margin-bottom:6px}
.cards i{width:22px;height:14px;border-radius:2px}
.ground{left:0;top:1090px;width:720px;height:110px;background:linear-gradient(180deg,rgba(255,255,255,0) 0,#e9f2cf 45%,#b8dd7a 100%)}
.fline{left:60px;top:1112px;width:600px;border-top:1px solid #ddd}
.copy{left:120px;top:1129px;font-size:7px;color:#444;font-family:Arial,sans-serif}
.copy a{color:var(--blue);text-decoration:none}
</style>
</head>
<body>
<div class="abs topstrip"></div>

<header>
  <div class="abs logo"><span class="logo-dot"></span><span class="logo-name">Velkor</span></div>
  <div class="abs follow">Follow us on:
    <i style="background:#3b5fa8"></i><i style="background:#3ab2e3"></i><i style="background:#4a7fc4"></i><i style="background:#f5901e"></i>
  </div>
  <div class="abs call">Call Us On: <b>123-456-7890</b></div>
  <div class="abs search">Search here...
    <svg width="11" height="11" viewBox="0 0 11 11"><circle cx="4.5" cy="4.5" r="3.4" fill="none" stroke="#222" stroke-width="1.4"/><line x1="7" y1="7" x2="10" y2="10" stroke="#222" stroke-width="1.6"/></svg>
  </div>
</header>

<nav class="abs nav">
  <ul>
    <li style="width:82px;text-align:center">Home</li>
    <li style="width:80px;text-align:center">About us</li>
    <li style="width:93px;text-align:center">Products</li>
    <li style="width:84px;text-align:center">Services</li>
    <li style="width:83px;text-align:center">Brands</li>
    <li style="width:70px;text-align:center">Blog</li>
    <li style="width:100px;text-align:center">Contact Us</li>
  </ul>
</nav>

<section class="abs banner">
  <div class="banner-inner">
    <div class="banner-photo" role="img" aria-label="Photo of a toddler playing with a colourful musical toy and a toy photo frame"></div>
    <div class="banner-title">Sesdiantda</div>
    <div class="banner-sub">Itaque earumrerus</div>
    <div class="banner-text">Temporibus autem quibusdam et aut offic aut rerum necessitatibus saepe eveniet</div>
    <div class="banner-btn">Shop Now</div>
    <div class="dots"><i></i><i></i><i></i><i></i><i></i></div>
  </div>
</section>

<h2 class="abs heading services">Our Services</h2>
<section class="abs service-row">
  <div class="service c-orange">
    <h3>Global Sourcing, Distribution<br>&amp; Supply Solutions</h3>
    <svg width="30" height="30" viewBox="0 0 30 30" fill="none" stroke="#f05a0a" stroke-width="1.6"><circle cx="15" cy="15" r="13"/><ellipse cx="15" cy="15" rx="6" ry="13"/><line x1="2" y1="15" x2="28" y2="15"/><line x1="15" y1="2" x2="15" y2="28"/><path d="M4 8h22M4 22h22"/></svg>
    <p>Lorem ipsum dolor sit amet, consectetur adipiscing elit Donec ullamcorper, turpis non iaculis bibendum, arcu massa suscipit elit, at venenatis mi lectus et velit.</p>
    <span class="readmore">Read More »</span>
  </div>
  <div class="service c-blue">
    <h3>Specialist Private Label<br>Manufacturing Facilities</h3>
    <svg width="34" height="30" viewBox="0 0 34 30" fill="#0e8fd8"><circle cx="11" cy="11" r="8"/><circle cx="11" cy="11" r="3" fill="#fff"/><circle cx="25" cy="19" r="6"/><circle cx="25" cy="19" r="2.2" fill="#fff"/><circle cx="13" cy="25" r="4"/><circle cx="13" cy="25" r="1.5" fill="#fff"/></svg>
    <p>Fusce feugiat ullamcorper libero, nec malesuada velit sodales eu. Sed sollicitudin mollis neque vulputate euismod. Duis quis nulla eget eros congue ornare.</p>
    <span class="readmore">Read More »</span>
  </div>
  <div class="service c-green">
    <h3>Strict Quality Assurance<br>Processes &amp; Certifications</h3>
    <svg width="34" height="30" viewBox="0 0 34 30"><rect x="1" y="2" width="32" height="22" fill="#4c9a1a"/><rect x="4" y="5" width="26" height="16" fill="#fff"/><circle cx="12" cy="12" r="4" fill="#4c9a1a"/><path d="M9 15l-1 9 4-2 4 2-1-9" fill="#4c9a1a"/><path d="M19 9h8M19 13h8M19 17h6" stroke="#4c9a1a" stroke-width="1.5"/></svg>
    <p>Vivamus venenatis est in eros facilisis accumsan. Pellen tesque quam risus, porta aliquam arcu eget, blandit imperdiet metus. Ut tristique sed magna vitae</p>
    <span class="readmore">Read More »</span>
  </div>
</section>

<h2 class="abs heading featured">Featured Products</h2>
<div class="abs arrows">‹›</div>
<section class="abs products">
  <div class="product"><div class="product-img" role="img" aria-label="Baby bottles and feeding accessories" style="background:linear-gradient(135deg,#f6c28a,#d9eef8 60%,#f0f4f6)"></div><div class="product-name">Infant Feeding and<br>Accessories</div><div class="viewmore">View More</div></div>
  <div class="product"><div class="product-img" role="img" aria-label="Pink infant clothing set" style="background:linear-gradient(135deg,#f7c3d8,#f49ac0 60%,#fbe3ec)"></div><div class="product-name">Infant Clothing</div><div class="viewmore">View More</div></div>
  <div class="product"><div class="product-img" role="img" aria-label="Pair of plush baby slippers" style="background:linear-gradient(135deg,#ead8bf,#c8a880 60%,#efe2cf)"></div><div class="product-name">Infant Gear</div><div class="viewmore">View More</div></div>
  <div class="product"><div class="product-img" role="img" aria-label="Maternity tops and dresses" style="background:linear-gradient(135deg,#e6d7c9,#8e2a2e 50%,#ece4da)"></div><div class="product-name">Maternity Wear</div><div class="viewmore">View More</div></div>
  <div class="product"><div class="product-img" role="img" aria-label="Coloured men's trunks" style="background:linear-gradient(180deg,#e2453c,#3e62c6 40%,#56c14a 75%,#333)"></div><div class="product-name">Mens Underwear</div><div class="viewmore">View More</div></div>
  <div class="product"><div class="product-img" role="img" aria-label="Stack of striped towels" style="background:linear-gradient(90deg,#e8c23a,#45a0c8 35%,#d9463c 65%,#68b04a)"></div><div class="product-name">Homewares and<br>Manchester</div><div class="viewmore">View More</div></div>
</section>

<h2 class="abs heading brands">Brands</h2>
<h2 class="abs heading quick">Quick Links</h2>
<section class="abs brand-grid">
  <div class="brand b1"><span class="brand-name">Wimbletots</span><p>Fun &amp; Amazing Value range of baby Clothing, Manchester and Accessories</p></div>
  <div class="brand b2"><span class="brand-name">Lunorella</span><p>Luxurious Organic Baby Clothing, Wraps and Accessories</p></div>
  <div class="brand b3"><span class="brand-name">Tinyharbor</span><p>Everything Baby at Amazing Prices</p></div>
  <div class="brand b4"><span class="brand-name">Faxlo Infant</span><p>Infant Feeding range with all your favourite Faxlo Characters</p></div>
  <div class="brand b5"><span class="brand-name">WovenHarvests</span><p>Luxury range of Towels and Manchester</p></div>
  <div class="brand b6"><span class="brand-name">ZigzagKite</span><p>Exciting range of Kids Clothing, with a twist</p></div>
</section>

<a class="abs tile tile-blog">
  <svg style="left:18px;top:24px" width="68" height="48" viewBox="0 0 68 48" fill="none" stroke="#fff" stroke-width="2.5"><path d="M34 8C25 3 12 3 3 6v38c9-3 22-3 31 2 9-5 22-5 31-2V6c-9-3-22-3-31 2z" fill="#fff" fill-opacity=".05"/><line x1="34" y1="8" x2="34" y2="46"/><path d="M10 15h17M10 21h17M10 27h17M10 33h17M41 15h17M41 21h17M41 27h17M41 33h17" stroke-width="1.5"/></svg>
  <span class="big" style="left:106px;top:20px">BLOG</span>
  <span class="small" style="left:108px;top:56px">➤ VISIT BLOG</span>
</a>
<a class="abs tile tile-shop">
  <svg style="left:18px;top:18px" width="64" height="62" viewBox="0 0 64 62" fill="none" stroke="#fff" stroke-width="4"><rect x="4" y="4" width="56" height="38" rx="3"/><rect x="2" y="48" width="60" height="10" rx="2"/><path d="M28 16l0 14 4-4 3 6 2-1-3-6 5 0z" fill="#fff" stroke-width="1"/></svg>
  <span class="big" style="left:98px;top:10px">SHOP<br>ONLINE</span>
  <span class="small" style="left:100px;top:68px">➤ SHOP NOW</span>
</a>

<footer>
  <div class="abs footer">
    <div class="fcol" style="left:18px">
      <h4>Information</h4>
      <ul><li>About Us</li><li>Services</li><li>Privacy Policy</li><li>Terms &amp; Condations</li><li>Contact Us</li></ul>
    </div>
    <div class="fsep" style="left:113px"></div>
    <div class="fcol" style="left:131px;width:130px">
      <h4>Blog</h4>
      <p>Contrary to popular belief Lorem Ipsum is not simply random text. It has roots in a piece of classical</p>
      <p style="margin-top:8px">Latin literature from 45 BC, making it over 2000 years old. Richard</p>
    </div>
    <div class="fsep" style="left:272px"></div>
    <div class="fcol" style="left:296px;width:130px">
      <h4>Contact Details</h4>
      <p>Velkor International<br>Lorem Ipsum is simply dummy text of the printing and typesetting</p>
      <p style="margin-top:8px">Tel: 123-456-7890<br>Email: info@velkor-example.com.au</p>
    </div>
    <div class="fsep" style="left:432px"></div>
    <div class="fcol" style="left:451px;width:135px">
      <h4>Secure Order Ststem</h4>
      <div class="payname">Paydrift</div>
      <div class="cards"><i style="background:#d9342b"></i><i style="background:#1a3f8f"></i><i style="background:#3a8bd0"></i><i style="background:#e8e8e8"></i></div>
      <p>You are safe when you buy with us as we use Paydrift to process all orders.</p>
    </div>
  </div>
  <div class="abs ground" role="img" aria-label="Illustrated meadow with grass, flowers, trees and bees"></div>
  <div class="abs fline"></div>
  <div class="abs copy">Copyright @ 2010 - 2013 <a>velkor-example.com.au</a> . All Rights Reserved</div>
</footer>
</body>
</html>
```